Fern Hollow Academy business card

we need to incorporate our school logo, name, address onto a great new school business card for all our staff - I included a lot of detail below under must haves and I included 3 business card samples below also that give a flavour of what I want - I would like to include a great graphic on at least one side of the card that represents education -

Target Market(s)

this business card will need to be attractive to parents of all ages but especially millennial parents and even high school students who may influence parents to chose Fern Hollow Academy

Industry/Entity Type

Education

Contact Information for Business Card

should contain core value words "curiosity kindness courage growth"
will need out school name, Fern Hollow Academy to be present, address 7281 Tamsworth Road, Burnaby, British Columbia V3K1P8
telephone 604.719.2083 Ext. 317
first card will need my name on it, Morvena Pelchuk, Director of Development & Operations
also web address of fernhollowacademy.ca

Font styles to use
Other font styles liked:
• Tw Cent MT

Requirements
Must have
• a fresh modern look for a private school environment that appeals to parents looking for great education - must use school logo, and incorporate colours navy blue, CMYK 100, 60, 0, 56 and burgundy CMYK 27, 98, 81, 50
• below I uploaded 3 business card layouts that look interesting to me - I'd like to incorporate some great school photos into the design - I tried to upload some school photos that we have, that the files are too large apparently? so I could send a link to Filecrate or something like that to share great high res pics that would look nice - we are kindergarten to Gr. 12 school, so I would like to include images that would represent great education at any age.
Nice to have
• spot colour would be nice as an option for printing for maybe key administrator business cards, while the rest would be basic printing

```html
<!DOCTYPE html>
<html lang="en">
<head>
<meta charset="utf-8">
<title>Fern Hollow Academy – Business Card</title>
<link rel="stylesheet" href="https://fonts.googleapis.com/css2?family=Jost:wght@400;500;600;700&display=swap">
<style>
  :root {
    --navy: #0f2d6b;
    --navy-deep: #0a1f4d;
    --burgundy: #6e1a2e;
    --ink-grey: #6b6b6b;
    --paper: #ffffff;
    --stage: #e9e9ec;
  }
  * { box-sizing: border-box; margin: 0; padding: 0; }
  html, body {
    width: 1200px; height: 766px; overflow: hidden;
    background: var(--stage);
    font-family: "Jost", "Century Gothic", sans-serif;
  }
  .stage {
    position: relative; width: 1200px; height: 766px;
    display: flex; align-items: center; justify-content: center; gap: 40px;
  }
  .card {
    position: relative; width: 520px; height: 297px; overflow: hidden;
    box-shadow: 0 6px 18px rgba(0,0,0,0.18);
  }

  /* Front: contact side */
  .card--front { background: var(--paper); }
  .card__edge { position: absolute; left: 0; top: 0; bottom: 0; width: 8px; background: var(--navy); }
  .card__tab { position: absolute; right: 0; bottom: 0; width: 8px; height: 70px; background: var(--burgundy); }

  .brand {
    position: absolute; top: 28px; right: 40px;
    display: flex; align-items: flex-start; gap: 10px;
  }
  .brand__mark { width: 34px; height: 34px; background: var(--navy); margin-top: 4px; }
  .brand__name {
    color: var(--burgundy); font-weight: 700; font-size: 20px;
    line-height: 0.95; text-transform: uppercase; letter-spacing: 0.5px;
  }

  .person { position: absolute; left: 44px; top: 100px; }
  .person__name {
    color: var(--burgundy); font-weight: 700; font-size: 15px;
    text-transform: uppercase; letter-spacing: 0.6px;
  }
  .person__title { color: var(--ink-grey); font-size: 10.5px; margin-top: 2px; }
  .person__address { color: var(--ink-grey); font-size: 10.5px; line-height: 1.45; margin-top: 14px; }

  .contact {
    position: absolute; right: 40px; bottom: 34px;
    list-style: none; font-size: 10.5px; line-height: 1.6; color: var(--ink-grey);
  }
  .contact__label { color: var(--burgundy); font-weight: 700; display: inline-block; width: 20px; }

  /* Back: values side */
  .card--back { background: var(--navy-deep); }
  .card__photo {
    position: absolute; inset: 0;
    background: linear-gradient(135deg, #2a3f7a 0%, #1c2f63 45%, #3a2c56 70%, #16275a 100%);
  }
  .card__photo::after {
    content: ""; position: absolute; inset: 0;
    background: rgba(15, 45, 107, 0.45);
  }
  .values {
    position: absolute; left: 0; right: 0; top: 118px;
    text-align: center; color: #fff;
    font-size: 27px; font-weight: 500; letter-spacing: 0.5px;
  }
</style>
</head>
<body>
  <main class="stage">
    <section class="card card--front" aria-label="Business card front">
      <div class="card__edge"></div>
      <div class="card__tab"></div>

      <div class="brand">
        <div class="brand__mark"></div>
        <div class="brand__name">Fern<br>Hollow<br>Academy</div>
      </div>

      <div class="person">
        <p class="person__name">Morvena Pelchuk</p>
        <p class="person__title">Director of Development &amp; Operations</p>
        <p class="person__address">7281 Tamsworth Rd<br>Burnaby, BC V3K 1P8</p>
      </div>

      <ul class="contact">
        <li><span class="contact__label">P:</span>604.719.2083 Ext. 317</li>
        <li><span class="contact__label">E:</span>mpelchuk@fernhollowacademy.ca</li>
        <li><span class="contact__label">W:</span>www.fernhollowacademy.ca</li>
      </ul>
    </section>

    <section class="card card--back" aria-label="Business card back">
      <div class="card__photo" role="img" aria-label="Photo of graduating students in caps and gowns with burgundy stoles, tinted navy"></div>
      <p class="values">curiosity kindness courage growth</p>
    </section>
  </main>
</body>
</html>
```